Training Brochure for Local Government Program needs a makeover and some creative design!

We would like our plain and boring brochure updated to be enticing for people to register for this program. Our organisation works in Local Government (Councils) in Australia and we are running our "leadership" program again in 2017.

We would like the brochure for this program to be engaging, bright and modern to entice the future leaders to participate.

The original file was created in Publisher, however we require the final file to be an easily editable PDF with front and back cover for updating in future years and for minor content changes.

It is not intended that this will be printed but made available electronically, however A4 size would be appreciated.

We require the following to be included
Our Logo (Supplied)
KWEN Logo (To be supplied within 48 hours)

Target Market(s)

Aspiring Leaders in Government
Young business minded people

Industry/Entity Type

Government

Font styles to use
Serif
Sans Serif
Decorative

Colors

Designer to choose colors to be used in the design.

Requirements
Must have
• Our Logo - Supplied
• The Facilitators logo (KWEN) - Supplied
Nice to have
• Our Corporate colours used
• Some nice photo's or use of icons etc

```html
<!DOCTYPE html>
<html lang="en">
<head>
<meta charset="utf-8">
<title>Emerging Leaders Program 2017 – Brochure Cover</title>
<link rel="stylesheet" href="https://fonts.googleapis.com/css2?family=Montserrat:wght@500;800&display=swap">
<style>
  :root {
    --green: #3f7a2a;
    --lime: #a9c63b;
    --yellow: #e5ae22;
    --orange: #d9782c;
    --navy: #1c4868;
    --ink-green: #2f6b2a;
    --ink-navy: #1d3f5e;
    --band: #f4f4f2;
    --bg: #6a6a68;
  }
  html, body {
    margin: 0;
    padding: 0;
    width: 1200px;
    height: 937px;
    overflow: hidden;
    background: var(--bg);
  }
  .cover {
    position: relative;
    width: 1200px;
    height: 937px;
    overflow: hidden;
    font-family: "Montserrat", Arial, sans-serif;
  }
  .stripes {
    position: absolute;
    inset: 0;
    display: flex;
  }
  .stripe { flex: 1; height: 100%; }
  .stripe--green  { background: linear-gradient(180deg, #4d8a33 0%, var(--green) 60%, #2c5a1d 100%); }
  .stripe--lime   { background: linear-gradient(180deg, #b8d24c 0%, var(--lime) 60%, #7f9a26 100%); }
  .stripe--yellow { background: linear-gradient(180deg, #f0bd33 0%, var(--yellow) 60%, #a97a12 100%); }
  .stripe--orange { background: linear-gradient(180deg, #e3893a 0%, var(--orange) 60%, #8f4a1a 100%); }
  .stripe--navy   { background: linear-gradient(180deg, #24567b 0%, var(--navy) 60%, #112d45 100%); }

  .title-band {
    position: absolute;
    left: 0;
    right: 0;
    top: 640px;
    height: 150px;
    background: var(--band);
    display: flex;
    align-items: center;
    padding: 0 60px;
    box-sizing: border-box;
  }
  .org-mark {
    display: flex;
    align-items: center;
    gap: 14px;
    width: 380px;
  }
  .org-mark__dot {
    width: 46px;
    height: 46px;
    border-radius: 50%;
    background: var(--ink-navy);
  }
  .org-mark__name {
    font-weight: 500;
    font-size: 24px;
    color: var(--ink-navy);
  }
  .program {
    margin-left: auto;
    text-align: right;
  }
  .partner-name {
    font-weight: 500;
    font-size: 22px;
    letter-spacing: 4px;
    color: var(--ink-navy);
    margin-bottom: 8px;
  }
  .program-title {
    margin: 0;
    font-weight: 800;
    font-size: 44px;
    letter-spacing: 1px;
    line-height: 1;
  }
  .program-title .w-emerging { color: var(--yellow); }
  .program-title .w-leaders  { color: var(--orange); }
  .program-title .w-program  { color: var(--ink-navy); }
  .program-title .w-year     { color: var(--ink-green); }
</style>
</head>
<body>
  <main class="cover">
    <div class="stripes">
      <div class="stripe stripe--green" role="img" aria-label="Photo of a senior businessman in a suit, tinted green"></div>
      <div class="stripe stripe--lime" role="img" aria-label="Photo of a young professional woman, tinted lime"></div>
      <div class="stripe stripe--yellow" role="img" aria-label="Photo of a young man in a suit and tie, tinted yellow"></div>
      <div class="stripe stripe--orange" role="img" aria-label="Photo of a professional woman in a blazer, tinted orange"></div>
      <div class="stripe stripe--navy" role="img" aria-label="Photo of a businessman in a dark suit, tinted navy"></div>
    </div>

    <section class="title-band">
      <div class="org-mark">
        <span class="org-mark__dot"></span>
        <span class="org-mark__name">Civic Leaders Network</span>
      </div>
      <div class="program">
        <div class="partner-name">KWEN</div>
        <h1 class="program-title">
          <span class="w-emerging">EMERGING</span>
          <span class="w-leaders">LEADERS</span>
          <span class="w-program">PROGRAM</span>
          <span class="w-year">2017</span>
        </h1>
      </div>
    </section>
  </main>
</body>
</html>
```